Poster design for a company operating care homes in the UK showcasing our core values

We need a poster to display in our care homes showcasing our new core values:

Purpose
We are driven by a clear understanding of why we do what we do: to enrich lives, honour legacies and make a meaningful difference every day, for our residents, their families, our colleagues and our community.

Excellence
We hold ourselves to the highest standards, delivering exceptional care and creating an environment where both residents and staff can thrive.

Openness
We build trust through honest, respectful communication, welcoming feedback, sharing ideas, and embracing change as a path to continuous growth.

Passion
We are passionate about delivering exceptional care. We take pride in what we do and in making a real difference in people’s lives.

Learning
We are committed to personal and professional growth; empowering each other through ongoing development, reflection, and shared knowledge.

Empathy
We actively listen and seek to understand before being understood, recognising the unique stories, feelings, and needs of others.

I have attached a small graphic that we would like you try to incorporate, in addition to our company logo. Please theme the rest of the poster around our company colours.

```html
<!DOCTYPE html>
<html lang="en">
<head>
<meta charset="utf-8">
<title>Our Core Values</title>
<link href="https://fonts.googleapis.com/css2?family=Fira+Sans:wght@400;600;700&display=swap" rel="stylesheet">
<style>
  :root {
    --bg: #f3ede3;
    --navy: #3b5573;
    --navy-soft: #4f6d80;
    --peach: #f2a688;
    --peach-soft: #f0ae8c;
  }
  * { margin: 0; padding: 0; box-sizing: border-box; }
  html, body { width: 1200px; height: 848px; overflow: hidden; background: var(--bg); }
  .poster {
    position: relative; width: 1200px; height: 848px; background: var(--bg);
    font-family: "Fira Sans", Arial, sans-serif; color: var(--navy);
  }
  .poster-title {
    position: absolute; left: 36px; top: 54px;
    font-size: 36px; font-weight: 700; color: var(--navy); letter-spacing: -0.3px;
  }
  .title-rule {
    position: absolute; left: 36px; top: 107px; width: 306px; height: 1.5px; background: var(--peach);
  }
  .brand {
    position: absolute; left: 862px; top: 44px; display: flex; align-items: center; gap: 12px;
  }
  .brand-mark { width: 42px; height: 42px; background: var(--navy); }
  .brand-name { font-size: 40px; font-weight: 600; color: var(--navy); letter-spacing: 0.5px; }
  .artwork { position: absolute; left: 0; top: 0; }
  .hex-letter {
    font-family: "Fira Sans", Arial, sans-serif; font-weight: 700; font-size: 58px;
  }
  .value { position: absolute; width: 190px; }
  .value h2 { font-size: 34px; font-weight: 600; line-height: 1; margin-bottom: 14px; letter-spacing: -0.2px; }
  .value p { font-size: 10.5px; line-height: 13px; }
  .navy-head h2 { color: var(--navy); }
  .navy-head p { color: var(--peach); }
  .peach-head h2 { color: var(--peach); }
  .peach-head p { color: var(--navy); }
  .value-purpose { left: 165px; top: 214px; width: 182px; }
  .value-openness { left: 481px; top: 214px; }
  .value-learning { left: 740px; top: 214px; }
  .value-excellence { left: 300px; top: 597px; }
  .value-passion { left: 605px; top: 597px; width: 180px; }
  .value-empathy { left: 860px; top: 597px; }
</style>
</head>
<body>
<main class="poster">
  <h1 class="poster-title">Our Core Values</h1>
  <div class="title-rule"></div>

  <div class="brand">
    <span class="brand-mark"></span>
    <span class="brand-name">HARROWBY</span>
  </div>

  <svg class="artwork" width="1200" height="848" viewBox="0 0 1200 848" aria-hidden="true">
    <defs>
      <linearGradient id="peachFill" x1="0" y1="0" x2="1" y2="0">
        <stop offset="0" stop-color="#f1ab8b"/>
        <stop offset="1" stop-color="#f4a586"/>
      </linearGradient>
      <linearGradient id="navyFill" x1="0" y1="0" x2="1" y2="0">
        <stop offset="0" stop-color="#547281"/>
        <stop offset="1" stop-color="#3a5472"/>
      </linearGradient>
      <filter id="hexShadow" x="-20%" y="-20%" width="140%" height="140%">
        <feDropShadow dx="0" dy="2" stdDeviation="3" flood-color="#000" flood-opacity="0.18"/>
      </filter>
      <polygon id="hex" points="-66,0 -34,-60 34,-60 66,0 34,60 -34,60"/>
    </defs>

    <g class="connector-lines" stroke="#f0a98a" stroke-width="1.2" fill="none">
      <polyline points="149,225 149,420 170,420"/>
      <line x1="467" y1="228" x2="467" y2="372"/>
      <line x1="724" y1="228" x2="724" y2="372"/>
      <polyline points="305,533 285,533 285,668"/>
      <line x1="590" y1="530" x2="590" y2="668"/>
      <line x1="846" y1="530" x2="846" y2="668"/>
    </g>

    <g class="hex-chain" filter="url(#hexShadow)" stroke-linejoin="round" stroke-width="12">
      <g transform="translate(275,423)">
        <use href="#hex" fill="url(#peachFill)" stroke="url(#peachFill)"/>
        <text class="hex-letter" y="21" text-anchor="middle" fill="#3b5573">P</text>
      </g>
      <g transform="translate(404,492)">
        <use href="#hex" fill="url(#navyFill)" stroke="url(#navyFill)"/>
        <text class="hex-letter" y="21" text-anchor="middle" fill="#f2a688">E</text>
      </g>
      <g transform="translate(531,423)">
        <use href="#hex" fill="url(#peachFill)" stroke="url(#peachFill)"/>
        <text class="hex-letter" y="21" text-anchor="middle" fill="#3b5573">O</text>
      </g>
      <g transform="translate(660,492)">
        <use href="#hex" fill="url(#navyFill)" stroke="url(#navyFill)"/>
        <text class="hex-letter" y="21" text-anchor="middle" fill="#f2a688">P</text>
      </g>
      <g transform="translate(787,423)">
        <use href="#hex" fill="url(#peachFill)" stroke="url(#peachFill)"/>
        <text class="hex-letter" y="21" text-anchor="middle" fill="#3b5573">L</text>
      </g>
      <g transform="translate(915,492)">
        <use href="#hex" fill="url(#navyFill)" stroke="url(#navyFill)"/>
        <text class="hex-letter" y="21" text-anchor="middle" fill="#f2a688">E</text>
      </g>
    </g>
  </svg>

  <section class="value value-purpose navy-head">
    <h2>Purpose</h2>
    <p>We are driven by a clear understanding of why we do what we do: to enrich lives, honour legacies and make a meaningful difference every day, for our residents, their families, our colleagues and our community</p>
  </section>

  <section class="value value-openness peach-head">
    <h2>Openness</h2>
    <p>We build trust through honest, respectful communication, welcoming feedback, sharing ideas, and embracing change as a path to continuous growth</p>
  </section>

  <section class="value value-learning navy-head">
    <h2>Learning</h2>
    <p>We are committed to personal and professional growth; empowering each other through ongoing development, reflection, and shared knowledge</p>
  </section>

  <section class="value value-excellence peach-head">
    <h2>Excellence</h2>
    <p>We hold ourselves to the highest standards, delivering exceptional care and creating an environment where both residents and staff can thrive</p>
  </section>

  <section class="value value-passion navy-head">
    <h2>Passion</h2>
    <p>We are passionate about delivering exceptional care. We take pride in what we do and in making a real difference in people’s lives</p>
  </section>

  <section class="value value-empathy peach-head">
    <h2>Empathy</h2>
    <p>We actively listen and seek to understand before being understood, recognising the unique stories, feelings, and needs of others</p>
  </section>
</main>
</body>
</html>
```